Faithful Oaks Fellowship (FOF)
• The Prayer arm of GRCA which enables members to delight themselves in the purpose and work of God
• Equip members with the instrument of prayer to walk with God so that they can make lasting changes here on Earth
• Coordinate projects like the Dawn Vigil Circle, Lantern Night Vigil Series, Chain Prayers, Prayer Projects, Prayer Retreats, and the Worldwide Vigil Circle
• Manage the GRCA Prayer Academy
• Goal is transformation and dominion
• Build members to stand as mighty men giving themselves continually to prayer

You learn how to pray by praying
Join the Faithful Oaks Fellowship!

```html
<!DOCTYPE html>
<html lang="en">
<head>
<meta charset="utf-8">
<title>Faithful Oaks Fellowship (FOF)</title>
<link href="https://fonts.googleapis.com/css2?family=Open+Sans:wght@400;700&family=Great+Vibes&display=swap" rel="stylesheet">
<style>
  :root {
    --navy: #0d4a7a;
    --green: #6fae2e;
    --white: #ffffff;
    --field-mist: #d9d2c6;
    --field-gold: #a8773c;
    --field-brown: #6b4520;
    --field-dark: #3a220d;
  }
  html, body {
    margin: 0;
    padding: 0;
    overflow: hidden;
    background: var(--white);
  }
  .poster {
    position: relative;
    width: 900px;
    height: 1200px;
    overflow: hidden;
    font-family: "Open Sans", Arial, sans-serif;
  }
  .poster-frame {
    position: absolute;
    inset: 0;
  }
  .brand {
    position: absolute;
    top: 82px;
    left: 170px;
    display: flex;
    align-items: center;
    gap: 28px;
  }
  .brand-dot {
    width: 170px;
    height: 170px;
    border-radius: 50%;
    border: 8px solid var(--navy);
    box-sizing: border-box;
  }
  .brand-name {
    font-family: "Great Vibes", cursive;
    font-size: 56px;
    line-height: 1.05;
    color: var(--navy);
    margin: 0;
  }
  .title {
    position: absolute;
    top: 345px;
    left: 0;
    width: 900px;
    text-align: center;
    margin: 0;
    color: var(--navy);
    font-weight: 700;
    font-size: 54px;
    letter-spacing: 0.5px;
  }
  .subtitle {
    position: absolute;
    top: 424px;
    left: 0;
    width: 900px;
    text-align: center;
    margin: 0;
    color: var(--navy);
    font-weight: 400;
    font-size: 34px;
  }
  .points {
    position: absolute;
    list-style: none;
    margin: 0;
    padding: 0;
    top: 0;
    left: 0;
    width: 900px;
    height: 1200px;
  }
  .point {
    position: absolute;
    width: 240px;
    color: var(--white);
    font-size: 18px;
    line-height: 1.18;
  }
  .point--a { left: 62px;  top: 607px; }
  .point--b { left: 312px; top: 607px; }
  .point--c { left: 596px; top: 607px; width: 250px; }
  .point--d { left: 62px;  top: 806px; }
  .point--e { left: 312px; top: 806px; }
  .point--f { left: 598px; top: 806px; }
  .tagline {
    position: absolute;
    top: 962px;
    left: 0;
    width: 900px;
    text-align: center;
    margin: 0;
    color: var(--white);
    font-weight: 700;
    font-size: 27px;
  }
  .invite {
    position: absolute;
    top: 1048px;
    left: 0;
    width: 900px;
    text-align: center;
    margin: 0;
    color: var(--white);
    font-family: "Great Vibes", cursive;
    font-size: 42px;
  }
</style>
</head>
<body>
<div class="poster">
  <svg class="poster-frame" width="900" height="1200" viewBox="0 0 900 1200" xmlns="http://www.w3.org/2000/svg">
    <defs>
      <linearGradient id="fieldTone" x1="0" y1="0" x2="0" y2="1">
        <stop offset="0" stop-color="#ffffff"/>
        <stop offset="0.2" stop-color="#ffffff"/>
        <stop offset="0.36" stop-color="var(--field-mist)"/>
        <stop offset="0.52" stop-color="var(--field-gold)"/>
        <stop offset="0.78" stop-color="var(--field-brown)"/>
        <stop offset="1" stop-color="var(--field-dark)"/>
      </linearGradient>
      <clipPath id="innerDisc">
        <circle cx="450" cy="600" r="706"/>
      </clipPath>
    </defs>
    <rect class="corner-fill" width="900" height="1200" fill="var(--green)"/>
    <circle class="frame-ring" cx="450" cy="600" r="716" fill="var(--navy)"/>
    <g clip-path="url(#innerDisc)">
      <rect width="900" height="1200" fill="var(--white)"/>
      <rect class="field-photo" role="img" aria-label="Photo of a golden meadow of wild grasses in soft morning light" x="0" y="0" width="900" height="1200" fill="url(#fieldTone)"/>
    </g>
  </svg>

  <header class="brand">
    <div class="brand-dot"></div>
    <p class="brand-name">Grace Rock<br>Christian Assembly</p>
  </header>

  <h1 class="title">FAITHFUL OAKS FELLOWSHIP</h1>
  <p class="subtitle">(FOF)</p>

  <ul class="points">
    <li class="point point--a">The Prayer arm of GRCA which enables members to delight themselves in the purpose and work of God</li>
    <li class="point point--b">Equip members with the instrument of prayer to walk with God so that they can make lasting changes here on Earth</li>
    <li class="point point--c">Coordinate projects like the Dawn Vigil Circle, Lantern Night Vigil Series, Chain Prayers, Prayer Projects, Prayer Retreats, and the Worldwide Vigil Circle</li>
    <li class="point point--d">Manage the GRCA Prayer Academy</li>
    <li class="point point--e">Goal is transformation and dominion</li>
    <li class="point point--f">Build members to stand as mighty men giving themselves continually to prayer</li>
  </ul>

  <p class="tagline">You learn how to pray by praying!</p>
  <p class="invite">Join the Faithful Oaks Fellowship!</p>
</div>
</body>
</html>
```